Website Design for my CNC machine Shop.

I need a new website for my Machining Company.

It can be a simple website that acts more like an "Online Business card" I has to highlight the services I provide and give Companies the confidence to engage my services.

I needs it to be a really modern or even a little futuristic promoting my Company.

I have just moved locations and have renovated the premises and would be great to let everyone know along with a new website.

If you can help with linking it to search engines to help get more exposure that would be great.

It needs to accommodate the three main services I provide which will include capacities of each machine (within that service) and maybe a couple images.
CNC Machining (5-axis, 3-axis)
EDM Wire cutting
3D Metal Printing
Along with home page and Contact page

I have two websites and you can use the txt from either/combination of these.
www.korvaltooling.com.au
(no longer do Laser Marking and etching but now do 3D metal Printing)
www.tarnquill.com.au

Happy to chat further with the designer

Company logo's provided.

For Images: I am happy to use Glimmerbay and can purchase any images you like
EDM Wire cut
https://www.glimmerbay-pics.com/search/edm-wire-cutting

CNC Machining:
https://www.glimmerbay-pics.com/search/vertical-cnc-machining
Don't use any with engines or motor vehicle parts

3D metal Printing
https://www.glimmerbay-pics.com/search/slm-metal-printing

Target Market(s)

Defence, Aerospace, Medical, HIgh Precision

Industry/Entity Type

Mechanical Engineering

Coding

Coded - Design and coding required

Number of Pages Required

5+ page

Requirements
Must have
• Home page, 3 services, Contacts. Can add image to each of the services

```html
<!DOCTYPE html>
<html lang="en">
<head>
<meta charset="utf-8">
<title>Korval Precision Machinists</title>
<link href="https://fonts.googleapis.com/css2?family=Teko:wght@400;500;600&family=Monoton&family=Inter:wght@400;500;600&display=swap" rel="stylesheet">
<style>
:root{
  --teal:#2bbf9f;
  --teal-dark:#23a98c;
  --ink:#1b1b1b;
  --slate:#4a5560;
  --paper:#f2f3f5;
  --white:#ffffff;
  --stage:#e6e6e6;
  --grey-text:#555b61;
}
*{box-sizing:border-box;margin:0;padding:0}
html,body{width:1200px;height:2948px;overflow:hidden;background:var(--stage)}
body{font-family:"Inter",Arial,sans-serif;color:var(--ink);position:relative}
.page{position:absolute;left:0;top:183px;width:1200px;height:2582px;background:var(--white);border-radius:14px;overflow:hidden}
.abs{position:absolute}

/* header */
.site-header{left:0;top:0;width:1200px;height:92px;background:var(--white)}
.brand{display:flex;align-items:center;gap:8px;font-family:"Teko",sans-serif;font-weight:600;font-size:40px;letter-spacing:3px;color:var(--slate);line-height:1}
.brand-mark{width:10px;height:10px;background:var(--teal)}
.site-header .brand{left:76px;top:28px}
.main-nav{left:355px;top:38px;font-size:10.5px;color:var(--ink)}
.main-nav span{position:absolute;white-space:nowrap}
.main-nav .active{color:var(--teal)}
.header-phone{left:866px;top:33px;display:flex;align-items:center;gap:7px;font-family:"Teko",sans-serif;font-size:17px;font-weight:500;white-space:nowrap;line-height:1}
.btn-quote{left:1014px;top:27px;width:111px;height:38px;background:var(--teal);color:var(--white);font-family:"Teko",sans-serif;font-size:13px;letter-spacing:.5px;display:flex;align-items:center;justify-content:center;white-space:nowrap}

/* hero */
.hero{left:0;top:92px;width:1200px;height:500px}
.hero-copy{left:0;top:105px;width:1200px;text-align:center;font-family:"Teko",sans-serif;color:var(--white);text-transform:uppercase}
.hero-copy .lead{font-size:34px;font-weight:400;line-height:53px}
.hero-copy .strong{font-size:42px;font-weight:600;line-height:53px}
.btn-outline-light{left:538px;top:282px;width:123px;height:37px;border:1.5px solid var(--white);color:var(--white);font-family:"Teko",sans-serif;font-size:12px;letter-spacing:.6px;display:flex;align-items:center;justify-content:center}
.slider-dots{left:563px;top:420px;display:flex;gap:9px}
.slider-dots i{width:9px;height:9px;border:1.3px solid var(--slate);border-radius:50%;display:block}
.slider-dots i.on{background:var(--slate);box-shadow:inset 0 0 0 2px var(--paper)}

/* welcome */
.welcome{left:0;top:403px;width:1200px;height:752px;background:var(--paper);z-index:0}
.welcome-photo{left:200px;top:659px;width:325px;height:387px;background:linear-gradient(150deg,#6f6a5e 0%,#c9c3b3 35%,#b78a3e 55%,#3d3a35 100%)}
.exp-badge{left:356px;top:904px;width:206px;height:174px;background:var(--teal);color:var(--white)}
.exp-badge .num{position:absolute;left:24px;top:22px;font-family:"Monoton",sans-serif;font-size:44px;line-height:1}
.exp-badge .yrs{position:absolute;left:122px;top:44px;font-family:"Teko",sans-serif;font-size:28px;font-weight:500}
.exp-badge .of{position:absolute;left:22px;top:92px;font-family:"Teko",sans-serif;font-size:28px;font-weight:500}
.exp-badge svg{position:absolute;left:0;top:0}
.eyebrow{font-size:17px;color:var(--teal);font-weight:400}
.display{font-family:"Monoton",sans-serif;font-weight:400;color:var(--slate);text-transform:uppercase;letter-spacing:1px}
.welcome-copy{left:612px;top:722px;width:400px}
.welcome-copy .display{font-size:27px;line-height:44px;margin-top:8px}
.welcome-copy p{font-size:14.2px;line-height:22.5px;color:var(--ink);margin-top:10px}
.welcome-copy b{font-weight:600}
.btn-outline-teal{left:612px;top:978px;width:125px;height:36px;border:1.5px solid var(--teal);color:var(--teal);font-family:"Teko",sans-serif;font-size:12px;letter-spacing:.6px;display:flex;align-items:center;justify-content:center}

/* services */
.services-head{left:0;top:1226px;width:1200px;text-align:center}
.services-head .display{font-size:24px;margin-top:6px}
.service-card{top:1310px;width:251px;height:314px;color:var(--white)}
.service-card .label{position:absolute;left:0;bottom:26px;width:100%;text-align:center;font-size:16px}
.card-cnc{left:200px;background:linear-gradient(160deg,#3c4a41 0%,#5d8a5c 35%,#2b2f31 100%)}
.card-edm{left:475px;background:linear-gradient(160deg,#2fc3a2 0%,#38c9a8 50%,#27b593 100%);text-align:center}
.card-edm h3{position:absolute;top:116px;width:100%;font-weight:400;font-size:17px}
.card-edm p{position:absolute;top:150px;left:18px;right:18px;font-size:12.2px;line-height:19px}
.card-edm .btn-light{position:absolute;left:69px;top:245px;width:112px;height:32px;background:var(--white);color:var(--teal);font-family:"Teko",sans-serif;font-size:12px;display:flex;align-items:center;justify-content:center}
.card-print{left:750px;background:linear-gradient(160deg,#24272a 0%,#6c7075 50%,#2c2f33 100%)}

/* contact */
.contact-band{left:0;top:1690px;width:1200px;height:515px}
.contact-copy{left:200px;top:1958px;width:370px}
.contact-copy .display{font-size:28px;color:#d8dde0;margin-top:4px}
.contact-copy p{color:var(--white);font-size:16.5px;line-height:22.5px;margin-top:18px}
.quote-form{left:612px;top:1888px;width:388px;height:367px;background:var(--teal);color:var(--white)}
.field{position:absolute;left:24px;width:340px;border-bottom:1px solid rgba(255,255,255,.85);font-size:10px;padding-bottom:9px}
.btn-send{position:absolute;left:132px;top:270px;width:100px;height:35px;border:1.3px solid var(--white);font-family:"Teko",sans-serif;font-size:12px;letter-spacing:.6px;display:flex;align-items:center;justify-content:center}

/* footer */
.site-footer{left:0;top:2205px;width:1200px;height:377px;background:var(--paper)}
.foot-col h4{font-weight:400;font-size:13px;margin-bottom:14px}
.foot-contact{left:405px;top:2320px}
.foot-contact .row{display:flex;gap:12px;align-items:flex-start;font-size:10px;line-height:17px;margin-bottom:10px}
.foot-contact .row.big{font-size:15px;line-height:20px}
.foot-links{left:613px;top:2320px;font-size:9.5px;line-height:19px}
.foot-hours{left:749px;top:2320px;font-size:9.5px;line-height:19px}
.foot-hours td{padding-right:26px;vertical-align:top}
.social{left:968px;width:32px;height:32px;border-radius:50%;background:var(--ink)}
.social.teal{background:var(--teal)}
.copyright{left:200px;top:2508px;font-size:9.5px}
.copyright span{color:var(--teal)}
.to-top{left:1092px;top:2501px}
</style>
</head>
<body>
<div class="page">

  <header class="site-header abs">
    <div class="brand abs"><span>KORVAL</span><i class="brand-mark"></i></div>
    <nav class="main-nav abs">
      <span class="active" style="left:0">-- HOME --</span>
      <span style="left:91px">CNC Machining</span>
      <span style="left:202px">EDM Wire Cutting</span>
      <span style="left:324px">3D Metal Printing</span>
      <span style="left:442px">Contact Us</span>
    </nav>
    <div class="header-phone abs">
      <svg width="13" height="13" viewBox="0 0 24 24"><path d="M6.6 10.8a15 15 0 0 0 6.6 6.6l2.2-2.2c.3-.3.7-.4 1-.2 1.1.4 2.3.6 3.6.6.6 0 1 .4 1 1V20c0 .6-.4 1-1 1A17 17 0 0 1 3 4c0-.6.4-1 1-1h3.5c.6 0 1 .4 1 1 0 1.3.2 2.5.6 3.6.1.3 0 .7-.2 1z" fill="#2bbf9f"/></svg>
      <span>+61 400 555 017</span>
    </div>
    <div class="btn-quote abs">REQUEST A QUOTE</div>
  </header>

  <section class="welcome abs"></section>

  <svg class="hero abs" width="1200" height="500" viewBox="0 0 1200 500" role="img" aria-label="Photo of a laser cutting head throwing sparks over a metal sheet">
    <defs>
      <linearGradient id="heroShade" x1="0" y1="0" x2="1" y2="1">
        <stop offset="0" stop-color="#3a3a3a"/>
        <stop offset=".45" stop-color="#262626"/>
        <stop offset=".7" stop-color="#4a3622"/>
        <stop offset="1" stop-color="#1c1c1c"/>
      </linearGradient>
    </defs>
    <polygon points="0,0 1200,0 1200,311 600,465 0,311" fill="url(#heroShade)"/>
    <polygon points="301,399 600,490 899,399 600,466" fill="#2bbf9f"/>
  </svg>

  <div class="hero-copy abs">
    <div class="lead">We are an innovative company that</div>
    <div class="strong">Specialise in technical and</div>
    <div class="strong">creative engineering</div>
  </div>
  <div class="btn-outline-light abs">CONTACT US</div>
  <div class="slider-dots abs"><i></i><i class="on"></i><i></i><i></i></div>

  <div class="welcome-photo abs" role="img" aria-label="Photo of a laser cutting a pattern into a steel plate"></div>
  <div class="exp-badge abs">
    <svg width="206" height="174" viewBox="0 0 206 174"><path d="M14 36V14h36M192 138v22h-36" fill="none" stroke="#fff" stroke-width="1.5"/></svg>
    <span class="num">20</span>
    <span class="yrs">YEARS</span>
    <span class="of">OF EXPERIENCE</span>
  </div>
  <div class="welcome-copy abs">
    <div class="eyebrow">Welcome to</div>
    <h1 class="display">Korval Precision<br>Machinists</h1>
    <p>Our core sectors of <b>expertise are in EDM wire cutting, Laser Etching/Marking and CNC machining.</b><br>With our combination of highly skilled staff and sophisticated machinery we offer a comprehensive and professional service.</p>
  </div>
  <div class="btn-outline-teal abs">REQUEST A QUOTE</div>

  <div class="services-head abs">
    <div class="eyebrow">What we do</div>
    <h2 class="display">Services we offer</h2>
  </div>
  <article class="service-card card-cnc abs" role="img" aria-label="Photo of a green vertical CNC machining centre in a workshop">
    <div class="label">CNC Machining</div>
  </article>
  <article class="service-card card-edm abs">
    <h3>EDM Wire Cutting</h3>
    <p>We operate Swiss manufactured Varnell EDM Machines which are regarded as the Aurentis of wire cut machines.</p>
    <div class="btn-light">EXPLORE MORE</div>
  </article>
  <article class="service-card card-print abs" role="img" aria-label="Photo of a grey 3D metal printed part">
    <div class="label">3D Metal Printing</div>
  </article>

  <svg class="contact-band abs" width="1200" height="515" viewBox="0 0 1200 515">
    <polygon points="0,188 600,31 1200,188 1200,515 0,515" fill="#000"/>
    <polygon points="301,101 600,12 899,101 600,28" fill="#2bbf9f"/>
  </svg>
  <div class="contact-copy abs">
    <div class="eyebrow">Get in touch</div>
    <h2 class="display">Request a quote</h2>
    <p>Please include your contact details and a short message and we will get back to you as soon as we can.</p>
  </div>
  <form class="quote-form abs">
    <div class="field" style="top:37px">Name</div>
    <div class="field" style="top:87px">Phone</div>
    <div class="field" style="top:137px">Email</div>
    <div class="field" style="top:187px;height:55px">Message ...</div>
    <div class="btn-send">SEND</div>
  </form>

  <footer class="site-footer abs"></footer>
  <div class="brand abs" style="left:200px;top:2338px"><span>KORVAL</span><i class="brand-mark"></i></div>
  <div class="foot-col foot-contact abs">
    <h4>Contact Us</h4>
    <div class="row big">
      <svg width="12" height="12" viewBox="0 0 24 24" style="margin-top:4px"><path d="M6.6 10.8a15 15 0 0 0 6.6 6.6l2.2-2.2c.3-.3.7-.4 1-.2 1.1.4 2.3.6 3.6.6.6 0 1 .4 1 1V20c0 .6-.4 1-1 1A17 17 0 0 1 3 4c0-.6.4-1 1-1h3.5c.6 0 1 .4 1 1 0 1.3.2 2.5.6 3.6.1.3 0 .7-.2 1z" fill="#2bbf9f"/></svg>
      <span>+61 400 555 017</span>
    </div>
    <div class="row">
      <svg width="12" height="12" viewBox="0 0 24 24" style="margin-top:3px"><rect x="3" y="6" width="18" height="12" rx="1" fill="#2bbf9f"/><path d="M3 7l9 6 9-6" fill="none" stroke="#fff" stroke-width="1.5"/></svg>
      <span>info@korvaltooling.com.au</span>
    </div>
    <div class="row">
      <svg width="12" height="12" viewBox="0 0 24 24" style="margin-top:3px"><path d="M12 2a7 7 0 0 0-7 7c0 5 7 13 7 13s7-8 7-13a7 7 0 0 0-7-7z" fill="#2bbf9f"/><circle cx="12" cy="9" r="2.5" fill="#fff"/></svg>
      <span>Unit 4, 18 Brennock Rd,<br>DANDELL, VIC 3999</span>
    </div>
  </div>
  <div class="foot-col foot-links abs">
    <h4>Quick Links</h4>
    <div>Home</div><div>About Us</div><div>CNC Machining</div><div>EDM Wire Cutting</div><div>3D Metal Printing</div><div>Contact Us</div>
  </div>
  <div class="foot-col foot-hours abs">
    <h4>Hours of Operation</h4>
    <table>
      <tr><td>Mon - Fri:</td><td>8:00 am - 5:00 pm</td></tr>
      <tr><td>Saturday:</td><td>By Appointment Only</td></tr>
      <tr><td>Sunday:</td><td>Closed</td></tr>
    </table>
  </div>
  <span class="social abs" style="top:2318px"></span>
  <span class="social teal abs" style="top:2355px"></span>
  <span class="social abs" style="top:2393px"></span>
  <div class="copyright abs">© 2024 <span>Korval Precision Machinists</span>. All Right Reserved</div>
  <svg class="to-top abs" width="16" height="18" viewBox="0 0 16 18"><path d="M8 0L16 18 8 13 0 18z" fill="#2bbf9f"/></svg>

</div>
</body>
</html>
```